Car Repair Business Website Redesign

We need a new design for our wordpress website, which generates traffic and converts leads for our car repair business. The site was originally setup with a blank template and the design was never tweaked. All content is in place, so the design needs to arrange existing content into a visually strong, responsive layout with top priority given to conversion. You can view the existing website at www.brisklanevanfix.com. Responsive design is extremely important - 36% of visitors are mobile and 18% tablet - so please include mobile designs.
To confirm, the brief is for PSD only, please supply designs for the following two pages:-
http://www.brisklanevanfix.com/
http://www.brisklanevanfix.com/clutch-replacement/
Target Market(s)
Predominantly male (75%), 25-55 year old (70%) audience.
Industry/Entity Type
Car Repair
Number of Pages Required
2 page
Requirements
Must have
- Good use of colour, clear design elements. Our competitors just had a re-design which although not perfect, displays many good elements: www.gearpok.com

```html
<!DOCTYPE html>
<html lang="en">
<head>
<meta charset="utf-8">
<title>Brisklane Van Fix</title>
<link href="https://fonts.googleapis.com/css2?family=Roboto:wght@400;500;700&family=Open+Sans:wght@400;600&display=swap" rel="stylesheet">
<style>
:root{
  --blue:#0b6fae;
  --blue-text:#0c69a6;
  --page:#e9ecf1;
  --panel:#ffffff;
  --panel-soft:#f6f7f9;
  --line:#e3e6ea;
  --ink:#333a40;
  --muted:#5a6168;
  --dark:#2c2f33;
}
*{box-sizing:border-box;margin:0;padding:0}
html,body{width:1129px;height:1200px;overflow:hidden}
body{background:linear-gradient(135deg,#eef0f4 0%,#e2e6ec 50%,#eef0f4 100%);font-family:"Open Sans",sans-serif;color:var(--ink);position:relative}
.box{position:absolute;background:var(--panel);border:1px solid var(--line)}
.heading{background:var(--blue);color:#fff;font-family:"Roboto",sans-serif;font-weight:400;text-transform:uppercase}
/* header */
.brand{left:34px;top:23px;width:308px;height:105px;display:flex;align-items:center;justify-content:center;flex-direction:column}
.brand-name{font-family:"Roboto",sans-serif;font-weight:700;font-size:44px;color:#1d1d1d;line-height:1}
.brand-sub{font-family:"Roboto",sans-serif;font-size:12px;letter-spacing:4px;color:#444;margin-top:6px}
.nav{left:360px;top:23px;width:737px;height:105px;display:flex}
.nav-item{height:100%;border-right:1px solid var(--line);display:flex;flex-direction:column;align-items:center;justify-content:center;font-family:"Roboto",sans-serif;font-size:15px;color:#222;gap:14px}
.nav-item svg{height:32px}
.call{flex:1;text-align:right;padding:20px 20px 0 0}
.socials{display:flex;gap:5px;justify-content:flex-end}
.socials span{width:22px;height:22px;border-radius:50%;display:block}
.call-label{font-family:"Roboto",sans-serif;font-size:15px;color:#333;margin-top:10px}
.call-number{font-family:"Roboto",sans-serif;font-size:18px;color:var(--blue-text);letter-spacing:.5px;margin-top:2px}
/* branch */
.branch{left:35px;top:157px;width:243px;height:680px}
.branch .heading{height:75px;display:flex;align-items:center;justify-content:center;text-align:center;font-size:19px;line-height:27px}
.map{position:absolute;left:16px;top:180px;width:210px;height:380px;background:radial-gradient(ellipse at 40% 35%,#3aa9ec 0%,#3aa9ec 35%,rgba(58,169,236,.25) 60%,transparent 72%)}
.search{position:absolute;left:0;bottom:0;width:100%;height:56px;border-top:1px solid var(--line);display:flex;align-items:center;justify-content:space-between;padding:0 20px 0 23px;font-size:13px;color:var(--blue-text)}
/* tiles */
.tile{position:absolute;width:273px;height:242px;color:#fff;text-align:center;overflow:hidden}
.tile .photo{position:absolute;inset:0;background:linear-gradient(160deg,#5a626b,#262a2f)}
.tile .num{position:relative;font-family:"Roboto",sans-serif;font-size:34px;margin-top:24px}
.tile .title{position:relative;font-family:"Roboto",sans-serif;font-size:22px;margin-top:10px}
.tile p{position:relative;font-size:13.5px;line-height:22px;margin:8px 26px 0;color:#eee}
.tile svg{position:relative;margin-top:18px}
/* reviews */
.reviews{left:288px;top:660px;width:558px;height:177px}
.reviews .heading{height:46px;line-height:46px;padding-left:21px;font-size:16px}
.avatar{position:absolute;left:28px;top:64px;width:104px;height:104px;border-radius:50%;border:3px solid #e5e7ea;background:linear-gradient(180deg,#cfd7de,#7e8a95)}
.quote{position:absolute;left:171px;top:68px;width:360px;font-size:13px;line-height:20px;color:var(--muted)}
.quote b{font-family:"Roboto",sans-serif;font-size:16px;color:#777;font-weight:700}
.reviewer{position:absolute;left:171px;top:134px;font-family:"Roboto",sans-serif;font-size:16px;color:var(--blue-text)}
/* help */
.help{left:854px;top:157px;width:244px;height:234px}
.help .heading{height:56px;line-height:56px;text-align:center;font-size:19px}
.help-link{height:59px;border-bottom:1px solid var(--line);display:flex;align-items:center;padding-left:28px;gap:12px;font-family:"Roboto",sans-serif;font-size:14px;color:var(--blue-text);letter-spacing:.3px}
.help-link:last-child{border-bottom:0}
.ring{width:32px;height:32px;border-radius:50%;border:1.5px solid var(--blue);display:flex;align-items:center;justify-content:center}
.why{left:854px;top:400px;width:244px;height:437px}
.why .heading{height:78px;display:flex;align-items:center;justify-content:center;text-align:center;font-size:19px;line-height:27px}
.post{padding:16px 16px 0 16px;height:120px;border-bottom:1px solid var(--line);font-size:12px;line-height:20px;color:var(--muted)}
.post:last-child{border-bottom:0;padding-top:24px}
.date{font-family:"Roboto",sans-serif;margin-top:6px;font-size:12px;color:#555;display:flex;align-items:center;gap:6px}
/* bottom row */
.clutch{left:35px;top:847px;width:526px;height:177px}
.clutch .heading,.faq .heading{height:46px;line-height:46px;padding-left:21px;font-size:16px}
.clutch h3{position:absolute;left:146px;top:68px;font-family:"Roboto",sans-serif;font-weight:400;font-size:16px;color:var(--blue-text)}
.clutch p{position:absolute;left:146px;top:98px;width:370px;font-size:12.5px;line-height:20px;color:var(--muted)}
.clutch svg{position:absolute;left:32px;top:66px}
.faq{left:571px;top:847px;width:526px;height:177px}
.part{position:absolute;top:63px;width:111px;height:97px;background:radial-gradient(circle at 50% 50%,#9aa1a9 0%,#c9ced4 40%,#e9ebee 70%)}
/* footer */
.footer{left:34px;top:1053px;width:1064px;height:117px;background:linear-gradient(90deg,#f7f8fa,#f1f3f5)}
.copy{position:absolute;left:24px;top:32px;font-size:14px;color:#333}
.links{position:absolute;left:25px;top:69px;font-size:14px;color:#333}
.links span{margin:0 6px;color:#555}
.foot-social{position:absolute;right:32px;top:44px;display:flex;gap:7px}
.foot-social span{width:27px;height:27px;border-radius:50%;display:block}
</style>
</head>
<body>

<header>
  <div class="box brand">
    <div class="brand-name">brisklane</div>
    <div class="brand-sub">VAN FIX MECHANICS</div>
  </div>
  <nav class="box nav">
    <div class="nav-item" style="width:127px">
      <svg viewBox="0 0 28 30" width="28"><circle cx="14" cy="8" r="7" fill="#0b6fae"/><path d="M1 29c0-8 6-12 13-12s13 4 13 12z" fill="#0b6fae"/></svg>
      ABOUT US</div>
    <div class="nav-item" style="width:148px">
      <svg viewBox="0 0 40 34" width="40"><g fill="#0b6fae"><circle cx="14" cy="19" r="9"/><circle cx="30" cy="9" r="6"/><circle cx="31" cy="26" r="5"/></g><g fill="#fff"><circle cx="14" cy="19" r="3.5"/><circle cx="30" cy="9" r="2.3"/><circle cx="31" cy="26" r="2"/></g><g stroke="#0b6fae" stroke-width="4"><path d="M14 7v24M2 19h24M5.5 10.5l17 17M22.5 10.5l-17 17"/></g><circle cx="14" cy="19" r="3.5" fill="#fff"/></svg>
      SERVICES</div>
    <div class="nav-item" style="width:148px">
      <svg viewBox="0 0 22 32" width="22"><path d="M11 1C5 1 1 5.5 1 11c0 7 10 20 10 20s10-13 10-20C21 5.5 17 1 11 1z" fill="#0b6fae"/><circle cx="11" cy="11" r="4" fill="#fff"/></svg>
      LOCATIONS</div>
    <div class="nav-item" style="width:118px">
      <svg viewBox="0 0 32 32" width="32"><circle cx="16" cy="16" r="15" fill="#111"/><path d="M11.5 12.5a4.5 4.5 0 1 1 6.5 4c-1.3.7-2 1.5-2 3" stroke="#fff" stroke-width="3" fill="none"/><circle cx="16" cy="24" r="2" fill="#fff"/></svg>
      FAQS</div>
    <div class="call">
      <div class="socials"><span style="background:#3b5998"></span><span style="background:#2aa3e0"></span><span style="background:#444"></span><span style="background:#f57d00"></span><span style="background:#e62117"></span></div>
      <div class="call-label">Call Us Today</div>
      <div class="call-number">0330 555 0182</div>
    </div>
  </nav>
</header>

<aside class="box branch">
  <div class="heading">Find your<br>closest branch</div>
  <div class="map" role="img" aria-label="Dotted map of North and South America showing branch regions"></div>
  <div class="search">City / Postcode
    <svg width="17" height="17" viewBox="0 0 17 17"><circle cx="7" cy="7" r="5.5" stroke="#666" stroke-width="2.2" fill="none"/><path d="M11 11l5 5" stroke="#666" stroke-width="2.6"/></svg>
  </div>
</aside>

<section class="tiles">
  <div class="tile" style="left:288px;top:158px">
    <div class="photo" role="img" aria-label="Mechanic in overalls holding a clipboard in a workshop"></div>
    <div class="num">01</div><div class="title">INSTANT QUOTE</div>
    <p>Proin gravida nibh vel velit auctor aliquet. Aenean sollicitudin, lorem quis bibendum auctor,</p>
    <svg width="20" height="20" viewBox="0 0 20 20"><path d="M2 3l8 7 8-7M2 10l8 7 8-7" stroke="#fff" stroke-width="2.4" fill="none"/></svg>
  </div>
  <div class="tile" style="left:572px;top:158px">
    <div class="photo" role="img" aria-label="Close-up of dark metal gear wheels" style="background:linear-gradient(160deg,#4a4d51,#1e2023)"></div>
    <div class="num">02</div><div class="title">INSTANT QUOTE</div>
    <p>Proin gravida nibh vel velit auctor aliquet. Aenean sollicitudin, lorem quis bibendum auctor,</p>
    <svg width="20" height="20" viewBox="0 0 20 20"><path d="M2 3l8 7 8-7M2 10l8 7 8-7" stroke="#fff" stroke-width="2.4" fill="none"/></svg>
  </div>
  <div class="tile" style="left:288px;top:409px">
    <div class="photo" role="img" aria-label="Hand holding a spanner" style="background:linear-gradient(160deg,#3d4a5a,#2a2f36)"></div>
    <div class="num">03</div><div class="title">INSTANT QUOTE</div>
    <p>Proin gravida nibh vel velit auctor aliquet. Aenean sollicitudin, lorem quis bibendum auctor,</p>
    <svg width="20" height="20" viewBox="0 0 20 20"><path d="M2 3l8 7 8-7M2 10l8 7 8-7" stroke="#fff" stroke-width="2.4" fill="none"/></svg>
  </div>
  <div class="tile" style="left:572px;top:409px">
    <div class="photo" role="img" aria-label="Mechanic working under a car bonnet" style="background:linear-gradient(160deg,#555b62,#24282d)"></div>
    <div class="num">04</div><div class="title">INSTANT QUOTE</div>
    <p>Proin gravida nibh vel velit auctor aliquet. Aenean sollicitudin, lorem quis bibendum auctor,</p>
    <svg width="20" height="20" viewBox="0 0 20 20"><path d="M2 3l8 7 8-7M2 10l8 7 8-7" stroke="#fff" stroke-width="2.4" fill="none"/></svg>
  </div>
</section>

<section class="box reviews">
  <div class="heading">Previous customers reviews</div>
  <div class="avatar" role="img" aria-label="Portrait of a customer in a suit"></div>
  <p class="quote"><b>“</b>&nbsp;&nbsp; Nulla sollicitudin tincidunt dui et egestas. Phasellus non sem tum, ullamcorper vitae, accumsan dui. Duis dignissim condi lorem. Maecenas facilisis ipsum sed porttitor rutrum. &nbsp;&nbsp;<b>”</b></p>
  <div class="reviewer">JOHN DOE</div>
</section>

<aside class="box help">
  <div class="heading">Need help?</div>
  <div class="help-link"><span class="ring"><svg width="14" height="12" viewBox="0 0 14 12"><path d="M2 8V6a5 5 0 0 1 10 0v2" stroke="#0b6fae" stroke-width="1.8" fill="none"/><rect x="1" y="7" width="3" height="4" fill="#0b6fae"/><rect x="10" y="7" width="3" height="4" fill="#0b6fae"/></svg></span>CHAT WITH US</div>
  <div class="help-link"><span class="ring"><svg width="12" height="12" viewBox="0 0 12 12"><path d="M2 1l2.5 0 1 3-1.5 1c.7 1.5 1.5 2.3 3 3l1-1.5 3 1V11C5 11 1 7 1 1z" fill="#0b6fae"/></svg></span>REQUEST A CALL BACK</div>
  <div class="help-link"><span class="ring"><svg width="12" height="12" viewBox="0 0 12 12"><path d="M2 1l2.5 0 1 3-1.5 1c.7 1.5 1.5 2.3 3 3l1-1.5 3 1V11C5 11 1 7 1 1z" fill="#0b6fae"/></svg></span>REQUEST A CALL BACK</div>
</aside>

<aside class="box why">
  <div class="heading">Why are we the<br>best choice?</div>
  <div class="post">Lorem ipsum dolor sit amet, conseetur adiing elit, sed do eiusmod tempor incididunt ut labore et dolore
    <div class="date"><svg width="13" height="11" viewBox="0 0 13 11"><path d="M1 5h3v6H1zM5 5l3-4c1 0 1.5.8 1.2 2L9 4.5h3l-1 6H5z" fill="#0b6fae"/></svg>APRIL 9, 2015</div></div>
  <div class="post">Lorem ipsum dolor sit amet, conseetur adiing elit, sed do eiusmod tempor incididunt ut labore et dolore
    <div class="date"><svg width="13" height="11" viewBox="0 0 13 11"><path d="M1 5h3v6H1zM5 5l3-4c1 0 1.5.8 1.2 2L9 4.5h3l-1 6H5z" fill="#0b6fae"/></svg>APRIL 9, 2015</div></div>
  <div class="post">Lorem ipsum dolor sit amet, conseetur adiing elit, sed do eiusmod tempor incididunt ut labore et dolore
    <div class="date"><svg width="13" height="11" viewBox="0 0 13 11"><path d="M1 5h3v6H1zM5 5l3-4c1 0 1.5.8 1.2 2L9 4.5h3l-1 6H5z" fill="#0b6fae"/></svg>APRIL 9, 2015</div></div>
</aside>

<section class="box clutch">
  <div class="heading">Do I need a clutch replacement?</div>
  <svg width="92" height="92" viewBox="0 0 92 92"><g fill="#0b6fae"><circle cx="46" cy="46" r="32"/><g id="t"><rect x="38" y="2" width="16" height="18" rx="2"/></g><use href="#t" transform="rotate(45 46 46)"/><use href="#t" transform="rotate(90 46 46)"/><use href="#t" transform="rotate(135 46 46)"/><use href="#t" transform="rotate(180 46 46)"/><use href="#t" transform="rotate(225 46 46)"/><use href="#t" transform="rotate(270 46 46)"/><use href="#t" transform="rotate(315 46 46)"/></g><circle cx="46" cy="46" r="14" fill="#fff"/></svg>
  <h3>Duis aute irure dolor in reprehenderit in voluptate</h3>
  <p>Nulla sollicitudin tincidunt dui et egestas. Phasellus non sem tum, ullamcorper vitae, accumsan dui. Duis dignissim condi lorem. Maecenas facilisis ipsum sed porttitor rutrum.</p>
</section>

<section class="box faq">
  <div class="heading">Freqently asked questions</div>
  <div class="part" style="left:20px" role="img" aria-label="Brake disc and caliper"></div>
  <div class="part" style="left:147px" role="img" aria-label="Clutch kit"></div>
  <div class="part" style="left:274px;background:radial-gradient(ellipse at 50% 50%,#e9ebee 0%,#4a4a4a 30%,#e9ebee 55%)" role="img" aria-label="Timing belt"></div>
  <div class="part" style="left:400px;background:linear-gradient(135deg,#d8dbdf,#6f757c)" role="img" aria-label="Metal gear wheels"></div>
</section>

<footer class="box footer">
  <div class="copy">©2014 - 2015 &nbsp;Brisklane Van Fix, All Rights Reserved.</div>
  <div class="links">Home <span>|</span> About Us <span>|</span> Services <span>|</span> FAQ <span>|</span>Contact Us</div>
  <div class="foot-social"><span style="background:#3b5998"></span><span style="background:#2aa3e0"></span><span style="background:#3f6ea5"></span><span style="background:#c8262c"></span></div>
</footer>

</body>
</html>
```